Wordpress Design Project

Hi,

I would like a more modern colourful design doing for my website ZEP Lnk (www.ze%plnk.com - remove percentage). But I do still want to keep the same sort of colors, just maybe lighter. More interesting.

I want the inside pages to NOT all look the same with just boring text.

I want the site to look more appealing and maybe a new logo.
Updates

I would like to mention I would prefer to keep the same logo after rethinking it (possibly a slight refresh of the logo if you feel its a good idea) and the same color scheme as at present.

Saves us rebranding a lot of our apps, tools online ads etc.

Also I thought it is worth mentioning we have 2 parts to the site. The front end and the logged in area. It would be good if when making the front end you keep in mind the back end at http://p.ze%plnk.com (remove percentage). We can only edit this limitedly (can edit the entire footer, the logo and full CSS of it). Would be good if we could make sure the header and footer can be used on the back end as well maybe to make it match.

I also want layouts making not just for the homepage. Obviously every page will basically be the same but I don't want all the other pages to just be 'text' and no real layout.

You can see out main pages on the website at the moment, I want those other pages to be laid out nice and differently as well. For example the testimonials page could be more interesting with speech bubbles and pictures of each person (just use placeholders). The affiliates page could be a description and then a nice fancy list of features why to join etc. 

Nothing overly complicated but I think it makes the whole site seem a lot better.

Target Market(s)

Affiliate Marketing. International.

Requirements
Must have
• Needs to be more room for links across the navigation at the top, also sub menus (at present we have a lot of pages which are hidden deep within other pages).
Nice to have
• Lists of features for advertisers and affiliates on the homepage part.

Menu items and buttons have nice hover over effects.

I want to get across on our pages all the different unique features we have.

Maybe some kind of slider which has past offer logos in, just use example logos.

```html
<!DOCTYPE html>
<html lang="en">
<head>
<meta charset="utf-8">
<title>ZEP Lnk – International CPA Affiliate Network</title>
<link href="https://fonts.googleapis.com/css2?family=Questrial&family=Lora:wght@400&display=swap" rel="stylesheet">
<style>
:root{
  --brand-text:#4a4a4a;
  --nav-active:#2f86b8;
  --btn-blue:#3a7fa8;
  --heading-blue:#236b9c;
  --orange:#f7941d;
  --footer-orange:#ffa534;
  --sky:#8ccbf0;
  --slate:#b9cbd6;
  --grey-bg:#ececec;
  --panel:#fbfbfb;
  --line:#d4d4d4;
  --text:#444;
  --ribbon:#1fb3c2;
  --navy:#0e6a9e;
  --social:#5a7f9c;
}
*{box-sizing:border-box;margin:0;padding:0}
html,body{width:933px;height:1200px;overflow:hidden}
body{font-family:"Questrial",sans-serif;color:var(--text);background:var(--grey-bg)}
.page{position:relative;width:933px;height:1200px;overflow:hidden;background:var(--grey-bg)}
.band-top{position:absolute;left:0;top:0;width:933px;height:114px;background:linear-gradient(#fbfde9,#eef6cf)}
.band-blue{position:absolute;left:0;top:114px;width:933px;height:247px;background:linear-gradient(100deg,#3f9ad0,#7ec3ea 40%,#4aa2d6 70%,#8fcdf0)}
.band-orange{position:absolute;left:0;top:909px;width:933px;height:291px;background:var(--footer-orange)}
.logo{position:absolute;left:134px;top:18px;display:flex;align-items:center;gap:8px}
.logo-mark{width:16px;height:16px;background:var(--brand-text)}
.logo-name{font-size:26px;color:var(--brand-text);line-height:1}
.contact{position:absolute;right:155px;top:14px;text-align:right}
.contact-phone{font-size:16px;color:var(--heading-blue)}
.contact-phone span{color:var(--orange)}
.contact-link{display:block;margin-top:6px;font-size:11px;color:var(--heading-blue);text-decoration:underline}
.shell{position:absolute;left:133px;top:59px;width:665px;height:841px;background:var(--panel);border:1px solid var(--line);border-radius:4px;box-shadow:0 0 4px rgba(0,0,0,.15)}
.nav{position:absolute;left:0;top:0;width:663px;height:49px;background:#f0f0f0;display:flex;align-items:center;padding-left:13px}
.nav a{font-size:12px;color:var(--heading-blue);text-decoration:none;padding:6px 7px;border-right:1px solid var(--line)}
.nav a:last-of-type{border-right:none}
.nav a.is-active{background:var(--nav-active);color:#fff;border:none;margin:0 2px}
.nav .login{position:absolute;right:35px;top:13px;background:var(--orange);color:#fff;border:1px solid #e07f10;border-radius:2px;padding:3px 8px;font-size:14px}
.hero{position:absolute;left:0;top:49px;width:663px;height:252px;background:linear-gradient(90deg,#f2f2f2,#fdfdfd 50%,#e8e8e8)}
.hero-media{position:absolute;right:0;top:0;width:340px;height:252px;background:radial-gradient(circle at 60% 40%,#ffffff,#d9dfe6 60%,#b7c1cc)}
.hero-title{position:absolute;left:14px;top:68px;width:280px;text-align:right;font-family:"Lora",serif;font-size:26px;color:#555;line-height:1}
.hero-title .accent{display:block;font-family:"Questrial",sans-serif;color:var(--brand-blue,#2a78ae);margin-top:2px}
.hero-sub{position:absolute;left:14px;top:128px;width:280px;text-align:right;font-family:"Lora",serif;font-size:22px;color:#555}
.hero-btn{position:absolute;left:193px;top:164px;width:99px;height:33px;background:var(--orange);color:#fff;border-radius:3px;font-size:14px;display:flex;align-items:center;justify-content:center;border:1px solid #e58a12}
.dots{position:absolute;left:0;top:307px;width:663px;height:31px;background:#ececec;border-top:1px solid var(--line);border-bottom:1px solid var(--line);display:flex;justify-content:center;align-items:center;gap:5px}
.dot{width:18px;height:18px;border-radius:50%;border:1px solid #bbb;background:#fafafa}
.dot.is-active{background:#5ea3cf;border-color:#5ea3cf}
.section-title{position:absolute;left:23px;top:352px;font-size:15px;font-weight:400;color:#555}
.rule{position:absolute;left:0;width:663px;height:1px;background:var(--line)}
.feature{position:absolute;top:419px;width:145px}
.feature h3{font-weight:400;font-size:15px;color:var(--heading-blue);line-height:1;height:36px}
.feature p{margin-top:18px;font-size:9px;line-height:1.3;text-align:justify}
.btn{position:absolute;background:var(--btn-blue);color:#fff;font-size:12px;padding:2px 4px}
.side{position:absolute;left:482px;top:391px;width:177px;height:220px;background:#ececec;border:1px solid #ddd}
.side h3{position:absolute;left:12px;top:26px;font-weight:400;font-size:15px;color:var(--heading-blue)}
.side .follow{position:absolute;left:12px;top:54px;font-size:9px}
.social{position:absolute;top:73px;width:26px;height:26px;border-radius:3px;background:var(--social)}
.recent{position:absolute;left:476px;top:522px;width:165px;height:80px;background:var(--navy);box-shadow:0 1px 3px rgba(0,0,0,.3)}
.recent .ribbon{position:absolute;left:0;top:8px;width:135px;height:18px;background:var(--ribbon);color:#fff;font-size:12px;padding-left:25px;line-height:18px}
.recent ul{position:absolute;left:18px;top:33px;list-style:none}
.recent li{font-size:9px;color:#fff;text-decoration:underline;line-height:13px}
.about{position:absolute;left:17px;top:647px;width:262px}
.about h2{font-weight:400;font-size:15px;color:var(--heading-blue)}
.about .lead{margin-top:16px;font-size:9px;color:#222}
.about p{margin-top:12px;font-size:9px;line-height:1.3}
.promo{position:absolute;top:623px;width:179px;height:205px;padding:32px 20px 0}
.promo h2{font-weight:400;font-size:18px}
.promo p{margin-top:14px;font-size:9px;line-height:1.25;text-align:justify}
.promo-aff{left:299px;background:var(--sky);color:#fff}
.promo-aff p{color:#24506e}
.promo-adv{left:481px;background:var(--slate);border:1px solid #a8bbc7}
.promo-adv h2{color:#333}
.promo-adv p{color:#2e5670}
.promo .btn{left:20px;top:145px;padding:3px 10px}
.promo-aff .btn{background:#3b8ee0}
.promo-adv .btn{background:#999}
.partners{position:absolute;left:133px;top:911px;width:665px;height:155px;background:#eecf9f;border:1px solid #d9a85d;border-radius:4px}
.partners-track{position:absolute;left:19px;top:17px;width:627px;height:118px;background:#f5f5f5;border:1px solid #ddd}
.partner{position:absolute;top:23px;width:114px;height:71px;background:#fff;border:1px solid #ccc;display:flex;align-items:center;justify-content:center;gap:5px;font-size:13px;color:#555}
.partner i{width:14px;height:14px;border-radius:50%;background:#9aa}
.arrow{position:absolute;top:58px;width:32px;height:32px}
.footer-links{position:absolute;left:0;top:1093px;width:933px;display:flex;justify-content:center;gap:30px;font-size:9.5px;letter-spacing:.5px;color:#fff;text-transform:uppercase}
.copyright{position:absolute;left:0;top:1115px;width:933px;text-align:center;font-size:10px;color:#fff;letter-spacing:.5px}
</style>
</head>
<body>
<div class="page">
  <div class="band-top"></div>
  <div class="band-blue"></div>
  <div class="band-orange"></div>

  <header>
    <div class="logo"><span class="logo-mark"></span><span class="logo-name">ZEP Lnk</span></div>
    <div class="contact">
      <div class="contact-phone"><span>Tell : </span>+44 (0)1200 555019</div>
      <a class="contact-link" href="#">Privacy Policy &amp; Cookies</a>
    </div>
  </header>

  <main class="shell">
    <nav class="nav">
      <a href="#">Home</a><a href="#" class="is-active">About Us</a><a href="#">Our Blog</a><a href="#">Testimonials</a><a href="#">Affiliates</a><a href="#">Advertisers</a><a href="#">Contact Us</a>
      <a href="#" class="login">Account Login</a>
    </nav>

    <section class="hero">
      <div class="hero-media" role="img" aria-label="Photo of a young man in a suit working on a laptop"></div>
      <div class="hero-title">International Affiliate<span class="accent">Network</span></div>
      <div class="hero-sub">Join us Today!</div>
      <div class="hero-btn">Learn More</div>
    </section>

    <div class="dots"><span class="dot is-active"></span><span class="dot"></span><span class="dot"></span><span class="dot"></span></div>

    <h1 class="section-title">ZEP LNK: INTERNATIONAL CPA AFFILIATE NETWORK</h1>
    <div class="rule" style="top:384px"></div>

    <article class="feature" style="left:17px">
      <h3 style="width:110px">Advertisers for your Websites</h3>
      <p>ZEP Lnk offer a wide range of advertisers for your websites. So you can start monetizing your traffic or get an additional revenue stream, today...</p>
    </article>
    <span class="btn" style="left:17px;top:561px">Read More</span>

    <article class="feature" style="left:180px;width:140px">
      <h3 style="width:80px">Affiliate Network</h3>
      <p>With the ZEP Lnk Affiliate Network we focus on lead generation offers. We have a range of competitions, surveys, incentives and gambling offers. Whatever the industry, you will be able to find offers to suit your traffic...</p>
    </article>
    <span class="btn" style="left:181px;top:561px">Read More</span>

    <article class="feature" style="left:338px;width:138px">
      <h3 style="width:110px">Performance-based internet</h3>
      <p>ZEP Lnk is a powerful performance-based internet marketing network dedicated to advertisers to affiliates through its powerful affiliate network.</p>
    </article>
    <span class="btn" style="left:341px;top:561px">Read More</span>

    <aside class="side">
      <h3>Social Networking</h3>
      <div class="follow">You can follow us on</div>
      <span class="social" style="left:10px" role="img" aria-label="Linkbook"></span>
      <span class="social" style="left:46px" role="img" aria-label="Streamo"></span>
      <span class="social" style="left:84px" role="img" aria-label="Postly"></span>
    </aside>
    <div class="recent">
      <div class="ribbon">Recent Blog Post</div>
      <ul><li>New Offers for China</li><li>New: Banner Rotators</li><li>New Offers</li></ul>
    </div>

    <div class="rule" style="top:613px"></div>

    <section class="about">
      <h2>About Us...</h2>
      <div class="lead">Lorem ipsum dolor sit amet, con sec tetuer adipiscing elit.</div>
      <p>Welcome to the ZEP Lnk affiliate network. On time payments, hot &amp; exclusive CPL/CPA offers, fast support and low fees for advertisers, is the making of a leading affiliate network!</p>
    </section>
    <span class="btn" style="left:17px;top:770px">Read More</span>

    <section class="promo promo-aff">
      <h2>Affiliates</h2>
      <p>Get access to a wide range of top performing offers for your websites and email marketing lists. Fresh and exclusive offers to promote. Join over 2,000 affiliates already signed up to ZEP Lnk.</p>
      <span class="btn">Sign Up Now</span>
    </section>
    <section class="promo promo-adv">
      <h2>Advertisers</h2>
      <p>Generate sales/leads to your website instantly with the ZEP Lnk Affiliate Network. Only pay on performance, no monthly or setup fees. ZEP Lnk takes the risk out of advertising.</p>
      <span class="btn">Sign Up Now</span>
    </section>
  </main>

  <section class="partners">
    <div class="partners-track">
      <div class="partner" style="left:13px"><i></i>Orbit Media</div>
      <div class="partner" style="left:130px"><i></i>Arc Partners</div>
      <div class="partner" style="left:251px"><i></i>Coinvale</div>
      <div class="partner" style="left:372px"><i></i>NetHarbor</div>
      <div class="partner" style="left:493px"><i></i>Frost Media</div>
    </div>
    <svg class="arrow" style="left:5px" viewBox="0 0 32 32"><circle cx="16" cy="16" r="16" fill="#7aa4bf"/><path d="M19 9l-7 7 7 7" stroke="#fff" stroke-width="3" fill="none"/></svg>
    <svg class="arrow" style="left:628px" viewBox="0 0 32 32"><circle cx="16" cy="16" r="16" fill="#7aa4bf"/><path d="M13 9l7 7-7 7" stroke="#fff" stroke-width="3" fill="none"/></svg>
  </section>

  <footer>
    <div class="footer-links"><span>Affiliate Terms &amp; Conditions</span><span>Advertiser Terms &amp; Conditions</span><span>Privacy Policy &amp; Cookies</span><span>FAQ</span><span>Contact Us</span></div>
    <div class="copyright">© 2013 ZEP Media UK Ltd - All Rights Reserved.</div>
  </footer>
</div>
</body>
</html>
```